General Dental Office Business Card

I run a private general dental office in southern California, and would like a refresh/redesign of my business card. I focus on quality care rather than volume. The email address on the uploaded current card should be updated to: info@marbleshoredental.example. The current card's logo is a deboss, but I am open to other ideas. The logo can be refreshed, but it is something that's been with me since the beginning of the office, so I wouldn't want a drastic redesign.
Target Market(s)
Adults 18-99, whoever needs dental services
Industry/Entity Type
Healthcare/Dental
Contact Information for Business Card
Name, Address, Phone, email
Colors
Designer to choose colors to be used in the design.
Requirements
Must have
- Logo (Same as original one in the uploaded file), space on back for appointment time/date

```html
<!DOCTYPE html>
<html lang="en">
<head>
<meta charset="utf-8">
<title>Marble Shore Dental – Business Card</title>
<link rel="stylesheet" href="https://fonts.googleapis.com/css2?family=Arimo:wght@400;700&display=swap">
<style>
:root{
  --aqua:#84d5ea;
  --ink:#5f5f5f;
  --rule:#8a8a8a;
  --band-grey:#737373;
  --paper:#ffffff;
  --backdrop:#e4e4e4;
}
*{margin:0;padding:0;box-sizing:border-box}
html,body{width:1125px;height:1200px;overflow:hidden;background:var(--backdrop);font-family:"Arimo",Arial,sans-serif;color:var(--ink)}
.card{position:absolute;left:150px;width:826px;height:472px;background:var(--paper);border-radius:22px;overflow:hidden}
.card--front{top:98px}
.card--back{top:631px}

.brand{position:absolute;left:560px;top:34px;width:200px;text-align:center}
.brand__dot{width:154px;height:154px;border-radius:50%;background:var(--aqua);margin:0 auto 12px}
.brand__name{font-size:38px;line-height:42px;color:var(--aqua);font-weight:400;white-space:nowrap;margin-left:-60px;margin-right:-60px}

.person{position:absolute;left:43px;top:218px}
.person__name{font-size:33px;font-weight:700;color:var(--aqua)}
.person__role{font-size:21px;margin-top:8px}
.divider{position:absolute;left:43px;top:303px;width:739px;height:2px;background:var(--rule)}

.contacts{position:absolute;left:43px;top:320px;list-style:none;font-size:21px}
.contacts li{display:flex;align-items:center;height:32.5px}
.contacts svg{width:18px;height:18px;margin-right:11px;flex:none}
.accent{color:var(--aqua)}
.address{position:absolute;right:44px;top:352px;text-align:right;font-size:21px;line-height:32.5px}
.foot-band{position:absolute;left:0;bottom:0;width:826px;height:20px}

.back-head{position:absolute;left:0;top:0;width:826px;height:169px;background:var(--aqua)}
.back-mark{position:absolute;left:338px;top:18px;width:144px;height:144px;border-radius:50%;background:var(--paper);display:flex;align-items:center;justify-content:center;text-align:center;font-size:17px;line-height:21px;color:var(--aqua)}
.back-rule{position:absolute;left:0;top:176px;width:826px;height:6px;background:var(--band-grey)}
.tab{position:absolute;left:210px;top:181px;width:400px;height:32px}
.tab__label{position:absolute;left:210px;top:181px;width:400px;height:32px;line-height:32px;text-align:center;color:#fff;font-size:22px;letter-spacing:.3px}
.write-line{position:absolute;left:55px;width:715px;border-top:1.5px dashed #a8a8a8}
.days{position:absolute;left:0;width:826px;top:348px;display:flex;justify-content:center;gap:26px;font-size:22px}
.slot{position:absolute;left:0;width:826px;top:386px;display:flex;justify-content:center;align-items:center;gap:12px;font-size:22px}
.check{display:inline-flex;align-items:center;gap:9px}
.check::before{content:"";width:17px;height:17px;border:2px solid var(--aqua);display:inline-block}
.blank{display:inline-block;border-bottom:1.5px solid var(--ink);height:24px}
</style>
</head>
<body>

<section class="card card--front" aria-label="Business card front">
  <div class="brand">
    <div class="brand__dot"></div>
    <div class="brand__name">Marble Shore<br>Dental</div>
  </div>

  <div class="person">
    <h1 class="person__name">Daniel R. Moore DDS</h1>
    <p class="person__role">General Dentistry</p>
  </div>
  <div class="divider"></div>

  <ul class="contacts">
    <li><svg viewBox="0 0 24 24" fill="none" stroke="#84d5ea" stroke-width="2"><path d="M5 3h4l2 5-2.5 1.5a11 11 0 0 0 6 6L16 13l5 2v4a2 2 0 0 1-2 2A17 17 0 0 1 3 5a2 2 0 0 1 2-2z"/></svg>949-555-0148</li>
    <li><svg viewBox="0 0 24 24" fill="none" stroke="#84d5ea" stroke-width="2"><rect x="3" y="5" width="18" height="14" rx="1"/><path d="M3 6l9 7 9-7"/></svg>info@marbleshoredental.example</li>
    <li><svg viewBox="0 0 24 24" fill="none" stroke="#84d5ea" stroke-width="1.8"><circle cx="12" cy="12" r="9"/><path d="M3 12h18M12 3c3 3 3 15 0 18M12 3c-3 3-3 15 0 18"/></svg>www.<span class="accent">marbleshoredental</span>.example</li>
  </ul>

  <address class="address" style="font-style:normal">1820 Harbor View Lane<br>Coastline, CA 92000</address>

  <svg class="foot-band" viewBox="0 0 826 20" preserveAspectRatio="none">
    <polygon points="0,4 568,4 552,20 0,20" fill="#84d5ea"/>
    <polygon points="584,4 826,4 826,20 568,20" fill="#737373"/>
  </svg>
</section>

<section class="card card--back" aria-label="Business card back">
  <div class="back-head"></div>
  <div class="back-mark">Marble Shore<br>Dental</div>
  <div class="back-rule"></div>
  <svg class="tab" viewBox="0 0 400 32"><polygon points="0,0 400,0 370,32 30,32" fill="#737373"/></svg>
  <div class="tab__label">APPOINTMENT</div>

  <div class="write-line" style="top:268px"></div>
  <div class="write-line" style="top:321px"></div>

  <div class="days">
    <span class="check">MON</span>
    <span class="check">TUE</span>
    <span class="check">WED</span>
    <span class="check">THU</span>
    <span class="check">FRI</span>
    <span class="check">SAT</span>
  </div>
  <div class="slot">
    <span>DATE</span><span class="blank" style="width:156px"></span>
    <span>TIME</span><span class="blank" style="width:104px"></span>
    <span class="check">AM</span><span class="check">PM</span>
  </div>
</section>

</body>
</html>
```